professional business card

A Clean looking business card for a money transfer company. Our company is call Velorix= Transfer + Send = Transcend (next level)
to show professionalism as well as some effects to show digital tech.

1 side to have position, name and address
2 side to have company name and show that we provide money exchange and cross-border money transfer

Target Market(s)

Remittance companies and high net worth individuals

Industry/Entity Type

Finance

Contact Information for Business Card

Name, address, email, title, services- money exchange and cross-border remittance

Requirements
Nice to have
• Digital age feel

```html
<!DOCTYPE html>
<html lang="en">
<head>
<meta charset="utf-8">
<title>Velorix Business Card</title>
<link href="https://fonts.googleapis.com/css2?family=Montserrat:wght@600;700&family=Open+Sans:wght@400;600&display=swap" rel="stylesheet">
<style>
  :root {
    --canvas: #dcdddf;
    --paper: #f1f1ef;
    --navy: #15223a;
    --cyan: #4cc3dc;
    --edge: #1e9fc7;
    --ink-soft: #6a6d72;
    --rule: #2a2f38;
    --white: #ffffff;
  }
  * { margin: 0; padding: 0; box-sizing: border-box; }
  html, body {
    width: 1200px;
    height: 1051px;
    overflow: hidden;
    background: var(--canvas);
  }
  .sheet {
    position: relative;
    width: 1200px;
    height: 1051px;
    display: flex;
    align-items: center;
    justify-content: center;
    gap: 40px;
  }
  .card {
    position: relative;
    width: 530px;
    height: 303px;
    border-radius: 3px;
    overflow: hidden;
    box-shadow: 0 14px 30px rgba(0, 0, 0, 0.18);
  }
  .card--front {
    background: var(--paper);
    border-bottom: 3px solid var(--edge);
  }
  .card--back {
    background: var(--navy);
    border-bottom: 3px solid var(--edge);
    display: flex;
    align-items: center;
    justify-content: center;
  }
  .brand {
    display: flex;
    align-items: center;
    gap: 12px;
    font-family: "Montserrat", sans-serif;
    font-weight: 700;
    letter-spacing: 0.04em;
    text-transform: uppercase;
  }
  .brand__dot {
    width: 22px;
    height: 22px;
    border-radius: 50%;
    background: var(--cyan);
    flex: none;
  }
  .card--front .brand {
    position: absolute;
    left: 34px;
    top: 92px;
    font-size: 30px;
    color: var(--navy);
  }
  .card--back .brand {
    font-size: 46px;
    color: var(--white);
  }
  .card--back .brand__dot { width: 30px; height: 30px; }
  .divider {
    position: absolute;
    left: 282px;
    top: 70px;
    width: 1px;
    height: 150px;
    background: var(--rule);
  }
  .contact {
    position: absolute;
    left: 302px;
    top: 72px;
    font-family: "Open Sans", sans-serif;
    color: var(--ink-soft);
    font-size: 12px;
    line-height: 1.45;
  }
  .contact__name {
    font-family: "Montserrat", sans-serif;
    font-weight: 700;
    font-size: 16px;
    color: var(--navy);
    letter-spacing: 0.03em;
    text-transform: uppercase;
  }
  .contact__title {
    color: var(--cyan);
    font-size: 13px;
    font-weight: 600;
    margin-bottom: 10px;
  }
  .contact__address { margin-bottom: 10px; }
  .contact__line {
    display: flex;
    align-items: center;
    gap: 7px;
  }
  .contact__line svg { width: 10px; height: 10px; flex: none; }
  .tagline {
    position: absolute;
    left: 34px;
    bottom: 26px;
    font-family: "Open Sans", sans-serif;
    font-size: 13px;
    color: var(--ink-soft);
  }
</style>
</head>
<body>
<main class="sheet">
  <section class="card card--front" aria-label="Card front">
    <div class="brand"><span class="brand__dot"></span>Velorix</div>
    <div class="divider"></div>
    <div class="contact">
      <p class="contact__name">Darren Holloway</p>
      <p class="contact__title">President</p>
      <p class="contact__address">1820 Harbor Crest Dr<br>Bayview CA 90412</p>
      <p class="contact__line">
        <svg viewBox="0 0 10 10" aria-hidden="true"><path d="M2 0.8 L3.6 2.6 L2.8 3.6 Q4 6 6.4 7.2 L7.4 6.4 L9.2 8 L8 9.4 Q3.5 9 0.6 2 Z" fill="var(--cyan)"/></svg>
        555-014-2783
      </p>
      <p class="contact__line">
        <svg viewBox="0 0 10 10" aria-hidden="true"><rect x="0.5" y="2" width="9" height="6.4" rx="0.8" fill="var(--cyan)"/><path d="M0.8 2.4 L5 5.6 L9.2 2.4" stroke="var(--paper)" stroke-width="0.9" fill="none"/></svg>
        d.holloway@velorix.com
      </p>
      <p class="contact__line">
        <svg viewBox="0 0 10 10" aria-hidden="true"><circle cx="5" cy="5" r="4.5" fill="var(--cyan)"/><path d="M0.5 5 H9.5 M5 0.5 Q2.4 5 5 9.5 M5 0.5 Q7.6 5 5 9.5" stroke="var(--paper)" stroke-width="0.7" fill="none"/></svg>
        www.velorix.com
      </p>
    </div>
    <p class="tagline">money exchange and cross-border remittance</p>
  </section>

  <section class="card card--back" aria-label="Card back">
    <div class="brand"><span class="brand__dot"></span>Velorix</div>
  </section>
</main>
</body>
</html>
```